Business Card and Letterhead Design for Public Accounting Firm

Business card and letterhead design for a CPA Firm located in Orange County, CA. We're looking for a modern and professional design utilizing our existing logo. We'd like a clean "less is more" look, but also something that catches the eye. We provide a high level of service to our clients. Open to single or double sided business cards.

Additional info: color numbers on logo
Blue :
R 0
G 83
B 125

#00537D

Silver :

R 154
G 154
B 154

#9A9A9A

Target Market(s)

Businesses and individuals

Industry/Entity Type

Accounting

Contact Information for Business Card

Moss Whitfield & Danby LLP - 4827 Larkspur Vale Road, Irvine, CA 92614 - (949)731-2864 - mwdaccts.example

Font styles to use
Serif
Sans Serif
Other font styles liked:
• See font file uploaded

Colors
0054AA
0677BA
7BADD7
CADEEF
E8F1F8

Requirements
Nice to have
• Possibly use the font file provided which matches our logo, but adjust to be not in all caps

```html
<!DOCTYPE html>
<html lang="en">
<head>
<meta charset="utf-8">
<title>Moss Whitfield &amp; Danby LLP – Stationery</title>
<link rel="stylesheet" href="https://fonts.googleapis.com/css2?family=Cinzel:wght@500&family=Figtree:wght@400;600&family=Lato:wght@400&display=swap">
<style>
  :root {
    --brand-blue: #0e4f7a;
    --brand-silver: #9a9a9a;
    --ink: #1f1f1f;
    --backdrop: #e3e3e3;
    --paper: #ffffff;
  }
  * { margin: 0; padding: 0; box-sizing: border-box; }
  html, body { width: 1200px; height: 1200px; overflow: hidden; background: var(--backdrop); }
  .canvas { position: relative; width: 1200px; height: 1200px; }

  .letterhead {
    position: absolute; left: 74px; top: 134px; width: 676px; height: 876px;
    background: var(--paper); overflow: hidden;
  }

  .wordmark {
    font-family: "Cinzel", serif; font-weight: 500; letter-spacing: .08em;
    line-height: 1.15;
  }
  .letterhead .wordmark {
    position: absolute; left: 67px; top: 58px; font-size: 17px; color: var(--brand-blue);
    display: flex; align-items: center; gap: 10px;
  }
  .mark-square { width: 14px; height: 14px; background: var(--brand-blue); flex: none; }

  .letter {
    position: absolute; left: 78px; top: 228px; width: 511px;
    font-family: "Lato", sans-serif; font-size: 10.2px; line-height: 13.2px; color: var(--ink);
  }
  .letter .salutation { margin-bottom: 40px; }
  .letter p { text-align: justify; margin-bottom: 13.2px; }

  .letter-footer {
    position: absolute; left: 0; top: 799px; width: 100%;
    font-family: "Figtree", sans-serif; font-size: 11px; line-height: 13.5px;
  }
  .letter-footer .col { position: absolute; }
  .strong-blue { color: var(--brand-blue); font-weight: 600; }
  .muted { color: #707070; }
  .phone-col { left: 109px; }
  .phone-col .phone { font-size: 13px; color: #707070; margin-top: 1px; }
  .address-col { left: 276px; top: 2px; }
  .web-col { left: 500px; top: 2px; }

  .card {
    position: absolute; left: 843px; width: 278px; height: 159px;
  }
  .card-front { top: 339px; background: var(--brand-blue); color: #fff; text-align: center; }
  .card-front .wordmark { position: absolute; left: 0; right: 0; top: 58px; font-size: 14px; color: #fff; }
  .card-front .tagline {
    position: absolute; left: 0; right: 0; top: 106px;
    font-family: "Figtree", sans-serif; font-size: 8px; color: #dce6ee; letter-spacing: .02em;
  }
  .card-back { top: 570px; background: var(--paper); }
  .card-back .wordmark {
    position: absolute; left: 22px; top: 68px; width: 120px; font-size: 8.5px; color: var(--brand-blue);
  }
  .card-back .contact {
    position: absolute; left: 158px; top: 58px;
    font-family: "Figtree", sans-serif; font-size: 7px; line-height: 9.4px; color: #555;
  }
  .card-back .contact .addr { color: var(--brand-blue); font-weight: 600; margin-bottom: 8px; }
  .card-back .contact b { color: var(--brand-blue); font-weight: 600; }
</style>
</head>
<body>
<div class="canvas">

  <section class="letterhead">
    <div class="wordmark"><span class="mark-square"></span><span>Moss Whitfield<br>&amp; Danby LLP</span></div>

    <div class="letter">
      <p class="salutation">Dear Sir/Madam</p>
      <p>Tum dis, aur. Iptisti entuius, cotia si imus ocuperio, qui pulinterorum ommo ia st diureo, qui pontem igit, querniq uemurnum iae tuus, quonst am popubliaci scerobu ssilne diendam se, Cata omantemorit, Catiam.</p>
      <p>Olut viviriv astique o nesicul ibunum pro, quon venatorum fex nos, nos, teritil intiae facie qua viti, que esci sente, orum is, quostam privis, clatquo publies hemus coena, quemuraverce nostesi llessen ationsus, seniusa tratque ressesilia inam ius, utu si porterf eculicu ssenter virmis aucemplia nondiem publius, Catusa tem prite audesum speridi orbisqua re, num tertum non Ita, se fatus etiae conem, caes? Ut Catimus, vis iam terrae, ut omprit vasdamquam pos nicas pulic temorum dinteritiam ipim intusquium utem pos, C. Reo, tabus, dium inprae tateridees? Ahabemn iciis.</p>
      <p>Dem teremus, que opos bon ad mus, Ti. Vivis; nosum patus bonsum audem mant verferris bonlocu tercepe ctempli cepontemur, efenius hemperunum, ut graet firmista se, quo con taredius ene anterfi catiam adeperio videper itilicu pplicis, ut gra ina, ne ex stum quidin de tam sum siti, senti, etifesus, fec re consulla re, con te moera nequa tam ommoventem publici verferv ignat, P. Fuius publicit vis, patiam delii ina, poris; hae, cuperce poteriure ia? Osto concus re o Catiferit, terei eores Ahabem aciam parest audam opotimm odiocae dienat, utus addum seniquit. Opionductuam tem tem intiactus, quamquer is. Effre inclus esuppli quideliu quo movis caeliaes omne mihDam in vis etiam noxim alius andiem hicaperum publist iortumus inatu que arbes auro esimus videt? Nihilibemus Ad mus.</p>
      <p>Verbis in vid fecrena turobse dem abenatre catus moena, cribult orisquonfec mantellem ute entissi linpris sum ampopub linatam publiem inatum moeres pro, Catique ignatia nonit, sul vicescrei por liissedetiam imed patiam te, dium non pra adestiam, C. Cupiocciam ommo entelabem quame ditiamdient? O tam no. Qui sin tant. Ut adhum patri essimus senatu mus es conduciae pre, ures constab efectori pre nihicie ntimperi coti, Ti. Verit nius ad alicatra, que pec temnovessi iam consultis.</p>
      <p>Ifes essenat iemnesc risquam haetil catince rfecien tilia? Ductord iorterusa talibem omnovere deret fuid facciam inem consupi ordium ta, que esimilinatu iam facte, sciondic octuita lempl. Am nocaperem iptessi ses! Sci pororurem ali paricaes consimacent. Mari pro corum hui te poptid conum es cum mo etiam publicieni portus, facepse taste dit viditas</p>
    </div>

    <footer class="letter-footer">
      <div class="col phone-col">
        <div class="strong-blue">Get in touch now</div>
        <div class="phone">(949)731-2864</div>
      </div>
      <div class="col address-col strong-blue">4827 Larkspur Vale Road,<br>Irvine, CA 92614</div>
      <div class="col web-col muted">
        <div><span class="strong-blue">E:</span> info@mwdaccts.example</div>
        <div><span class="strong-blue">W:</span> www.mwdaccts.example</div>
      </div>
    </footer>
  </section>

  <section class="card card-front">
    <div class="wordmark">Moss Whitfield<br>&amp; Danby LLP</div>
    <div class="tagline">Certified Public Accountants</div>
  </section>

  <section class="card card-back">
    <div class="wordmark">Moss Whitfield<br>&amp; Danby LLP</div>
    <div class="contact">
      <div class="addr">4827 Larkspur Vale Road,<br>Irvine, CA 92614</div>
      <div><b>T:</b> (949)731-2864</div>
      <div><b>E:</b> info@mwdaccts.example</div>
      <div><b>W:</b> mwdaccts.example</div>
    </div>
  </section>

</div>
</body>
</html>
```